Catalogue des écoles de langues partenaires de Morvaleck

Who are we ?
The group has 3 Morvaleck training facilities that could be established in Tunisia in recent years: Morvaleck, Bristane and Pluvemor.
What do we offer?
A wide range of services for all those interested in the German language training, career counseling, translation, assitance start ... The Morvaleck group offers help at every stage.
We need a new 2016 catalog of language schools Morvaleck partners in our business.
This is based on the old catalog 2015, but with some modifications, including the Design level, catalog text and the list of partner schools that will be updated.
The idea is to make this catalog a guide that comes in direct contact with the customer that will read the catalog.
The purpose of this catalog is to create a direct relationship with the customer who will read to choose later the city and school that suit him.
The catalog contains roughly 3/4 sections:
* 1st section: the first pages "standards" of our brochure, here we leave the old model to add a few details and change the design and organization;
the logo, the German flag, catalog name, address for making contact with Morvaleck,
the summary, the map of Germany with cities on the departments where Morvaleck has partner schools
All this will not fail in our catalog
*2nd section:
Presentation cities where Morvaleck partner language schools are located
Here is a description of the city, pictures of the city and language schools list without going into details of each school
3rd section:
Part 1: Overview of language schools partner Morvaleck by our "guide" team that will accompany us in this section, there will be a representative from each school that is located in several cities
An overview of the school, the services (we leave the old model), the location of the school in every German city (google map photo), housing highlighted !!!!
The cultural prog perhaps?
Part 2: everything about the course:
max number of people in each class levels (page 3 of the old model), review KLO Centre or not, units per week, intensive courses, super intensive courses, prices ???course dates,
dsh - daf difference? Registration tips, links, ... a few tips
Quote " Ubung macht den Meister " for example
* 4th section and last section:
under the title of "1st Steps in Germany"
* What to do upon arrival
* Basic vocabulary (discussion circle, representatives from each school)
* Say goodbye, good luck .. Germany, photo, dream, travel ..
> Sayings of the whole team and bubbles!!!!
> We would like a design in shades of green of our logo !! (really important)
We take the example of a page of this catalog in this section.
The page consists of several parts:
School description, super intensive and intensive courses
Date of the beginning and the end of each session in this school
School Location (pictured google map)
A table that includes:
Room, kitchen, linen and towels, common area, distance to campus , the prices ,units per week
(See attached file )

```html
<!DOCTYPE html>
<html lang="en">
<head>
<meta charset="utf-8">
<title>Morvaleck Catalog 2016-17</title>
<link rel="stylesheet" href="https://fonts.googleapis.com/css2?family=Ubuntu:wght@300;400;500;700&family=Lato:wght@400;700&display=swap">
<style>
  :root {
    --backdrop: #dcdcdc;
    --paper: #e7e7e7;
    --lime: #d3cf1f;
    --charcoal: #58585b;
    --ink: #3a3a3c;
    --navy: #2c4b9a;
    --white: #ffffff;
  }
  html, body {
    margin: 0;
    padding: 0;
    width: 1200px;
    height: 825px;
    overflow: hidden;
    background: var(--backdrop);
  }
  .cover {
    position: absolute;
    left: 324px;
    top: 22px;
    width: 552px;
    height: 780px;
    background: var(--paper);
    box-shadow: 0 6px 18px rgba(0,0,0,0.18);
    overflow: hidden;
    font-family: "Lato", sans-serif;
  }
  .cover-art {
    position: absolute;
    inset: 0;
    width: 552px;
    height: 780px;
  }
  .title-block {
    position: absolute;
    left: 112px;
    top: 390px;
    font-family: "Ubuntu", sans-serif;
  }
  .title-block .catalog-name {
    margin: 0;
    font-size: 31px;
    font-weight: 700;
    color: var(--charcoal);
    letter-spacing: 0.2px;
  }
  .title-block .catalog-year {
    margin: 4px 0 0;
    font-size: 27px;
    font-weight: 300;
    color: var(--white);
  }
  .title-block .tagline {
    margin: 10px 0 0 14px;
    font-size: 13px;
    font-weight: 400;
    color: var(--white);
    letter-spacing: 0.4px;
  }
  .intro {
    position: absolute;
    left: 296px;
    top: 664px;
    width: 232px;
  }
  .intro h2 {
    margin: 0 0 4px;
    font-family: "Lato", sans-serif;
    font-size: 13px;
    font-weight: 700;
    color: var(--navy);
  }
  .intro p {
    margin: 0;
    font-size: 8px;
    line-height: 1.45;
    color: var(--ink);
  }
  .brand {
    position: absolute;
    left: 70px;
    top: 690px;
    display: flex;
    align-items: center;
    gap: 8px;
  }
  .brand-dot {
    width: 26px;
    height: 26px;
    border-radius: 50%;
    background: var(--lime);
  }
  .brand-name {
    font-family: "Ubuntu", sans-serif;
    font-size: 20px;
    font-weight: 700;
    color: var(--charcoal);
  }
</style>
</head>
<body>
  <article class="cover">
    <svg class="cover-art" viewBox="0 0 552 780" xmlns="http://www.w3.org/2000/svg">
      <defs>
        <linearGradient id="campus-tones" x1="0" y1="0" x2="1" y2="1">
          <stop offset="0" stop-color="#6f8f4a"/>
          <stop offset="0.45" stop-color="#a9b86a"/>
          <stop offset="0.75" stop-color="#4f6fa8"/>
          <stop offset="1" stop-color="#3e4f7a"/>
        </linearGradient>
        <radialGradient id="study-tones" cx="0.5" cy="0.5" r="0.6">
          <stop offset="0" stop-color="#e8ddd0"/>
          <stop offset="1" stop-color="#9c8470"/>
        </radialGradient>
        <radialGradient id="classroom-tones" cx="0.5" cy="0.5" r="0.6">
          <stop offset="0" stop-color="#b9c6b8"/>
          <stop offset="1" stop-color="#6d6a66"/>
        </radialGradient>
      </defs>

      <path class="lime-band" d="M0 300 L552 300 L552 540 L0 590 Z" fill="var(--lime)"/>

      <path class="hero-photo" role="img" aria-label="Photo of a smiling student holding folders on a sunny campus path, with classmates behind"
            d="M0 0 H552 V334 Q300 300 0 324 Z" fill="url(#campus-tones)"/>

      <g class="tile-accents" fill="#ffffff">
        <rect x="330" y="345" width="70" height="42" rx="6" opacity="0.22"/>
        <rect x="372" y="372" width="72" height="44" rx="6" opacity="0.25"/>
        <rect x="420" y="318" width="60" height="40" rx="6" opacity="0.3"/>
        <rect x="442" y="355" width="66" height="46" rx="6" opacity="0.28"/>
        <rect x="468" y="300" width="60" height="44" rx="6" opacity="0.2"/>
        <rect x="405" y="350" width="40" height="30" rx="5" opacity="0.35"/>
      </g>

      <path class="web-strip" d="M0 576 L300 550 L300 563 L0 590 Z" fill="var(--charcoal)"/>
      <path class="corner-tab" d="M505 534 L552 530 L552 542 L505 546 Z" fill="var(--charcoal)"/>
      <text x="56" y="579" transform="rotate(-4.9 56 579)" font-family="Lato, sans-serif" font-size="9" letter-spacing="2" fill="#ffffff">www.morvaleck.org</text>

      <circle cx="345" cy="592" r="62" fill="url(#study-tones)" stroke="var(--paper)" stroke-width="6"
              role="img" aria-label="Photo of two students laughing together at a study table"/>
      <circle cx="470" cy="544" r="70" fill="url(#classroom-tones)" stroke="var(--paper)" stroke-width="6"
              role="img" aria-label="Photo of a classroom with students seated at desks and a teacher"/>
    </svg>

    <header class="title-block">
      <h1 class="catalog-name">Morvaleck Catalog</h1>
      <p class="catalog-year">2016- 17</p>
      <p class="tagline">Mauris ac dui nibh condimen metus</p>
    </header>

    <section class="intro">
      <h2>Lorem ipsum dolor sit amet elit</h2>
      <p>Mauris ac dui nibh, a condimentum metus. Mauris ante tortor adipiscing at porta tempus, commodo vel ipsum. Nam elementum tellus interdum consectetur venenatis, diam quam eleifend risus, sit amet pulvinar lectus erat a nibh suspendisse potenti.</p>
    </section>

    <div class="brand">
      <span class="brand-dot"></span>
      <span class="brand-name">Morvaleck group</span>
    </div>
  </article>
</body>
</html>
```